Letterhead and envelopes

hello Guys
We need a letterhead and envelope. Would like a clean and modern look. Simple, clean, elegant and professional.
We already have a logo and color scheme (see website), however we don't currently have a professional corp letterhead.

The letterhead should be 216mm x 303mm
Envelope should be 230mm x 120mm

The winner will deliver:

1) JPG, PNG, TIFF, PDF, Ai, EPS, PSD format files.
The work product will be an Illustrator or Photoshop file

CMYK, 300 dpi, convert fonts into paths (vector paths)
set margins at least 4 mm away from the edges

See attached files.

Good luck and let me know if you have any other questions.
Thank you

```html
<!DOCTYPE html>
<html lang="pt">
<head>
<meta charset="utf-8">
<title>Nexo Painéis — Letterhead</title>
<link href="https://fonts.googleapis.com/css2?family=Open+Sans:wght@400;600&display=swap" rel="stylesheet">
<style>
  :root {
    --backdrop: #d8d2cf;
    --paper: #ffffff;
    --brand-orange: #f0892a;
    --ink: #4a4a4a;
    --icon-ink: #ffffff;
  }
  * { box-sizing: border-box; margin: 0; padding: 0; }
  html, body {
    width: 1200px;
    height: 784px;
    overflow: hidden;
    background: var(--backdrop);
    font-family: "Open Sans", Arial, sans-serif;
  }
  .letterhead {
    position: absolute;
    left: 343px;
    top: 32px;
    width: 514px;
    height: 720px;
    background: var(--paper);
    box-shadow: 0 2px 6px rgba(0,0,0,0.12);
  }
  .brand {
    position: absolute;
    top: 44px;
    right: 44px;
    display: flex;
    align-items: center;
    gap: 10px;
    color: var(--brand-orange);
  }
  .brand-dot {
    width: 14px;
    height: 14px;
    border-radius: 50%;
    background: var(--brand-orange);
  }
  .brand-name {
    font-size: 26px;
    font-weight: 600;
    letter-spacing: 0.5px;
    line-height: 1;
  }
  .contact-block {
    position: absolute;
    left: 28px;
    bottom: 40px;
    display: flex;
    gap: 10px;
    align-items: stretch;
  }
  .icon-strip {
    width: 22px;
    background: var(--brand-orange);
    display: flex;
    flex-direction: column;
    justify-content: space-around;
    align-items: center;
    padding: 6px 0;
  }
  .icon-strip svg {
    width: 12px;
    height: 12px;
    fill: none;
    stroke: var(--icon-ink);
    stroke-width: 1.6;
  }
  .contact-lines {
    list-style: none;
    font-size: 8.5px;
    line-height: 13px;
    color: var(--ink);
  }
</style>
</head>
<body>
  <main class="letterhead">
    <header class="brand">
      <span class="brand-dot"></span>
      <span class="brand-name">Nexo Painéis</span>
    </header>

    <footer class="contact-block">
      <div class="icon-strip">
        <svg viewBox="0 0 12 12" aria-label="Endereço">
          <path d="M6 11 C3 7.5 2 6 2 4.5 A4 4 0 0 1 10 4.5 C10 6 9 7.5 6 11 Z"/>
          <circle cx="6" cy="4.5" r="1.3"/>
        </svg>
        <svg viewBox="0 0 12 12" aria-label="Telefone">
          <path d="M3 1.5 L5 3.8 L4 5 C4.8 6.6 5.6 7.4 7 8 L8.2 7 L10.5 9 L9.3 10.5 C5.5 10 2 6.5 1.5 2.7 Z"/>
        </svg>
        <svg viewBox="0 0 12 12" aria-label="Site">
          <circle cx="6" cy="6" r="4.5"/>
          <ellipse cx="6" cy="6" rx="2" ry="4.5"/>
          <line x1="1.5" y1="6" x2="10.5" y2="6"/>
        </svg>
      </div>
      <ul class="contact-lines">
        <li>Rua das Acácias 214, Sala 3</li>
        <li>04512-030 São Paulo Brasil</li>
        <li>+55 11 4321 0987</li>
        <li>(11) 9 8765 4321</li>
        <li>ID: 7046218835</li>
        <li>contato@nexopaineis.com.br</li>
        <li>www.nexopaineis.com.br</li>
      </ul>
    </footer>
  </main>
</body>
</html>
```